Brightwell Bonds and Households Initiative

We need a flyer that invites low-income Spanish speaking individuals to our program. The program is 12 weeks. We offer healthy relationship education, and financial stability. We also touch on workforce development. These workshops are for couples only.

We are in five locations, so we need a flyer that we can change the text to be able to update the address, dates and any additional information based on our needs.

Attached is the logo we would like to use. I have also attached a previous flyer that we created to give you an idea of the text that is included.

Target Market(s)

We are reaching out to low income adult couples

Font styles to use
Serif

Requirements
Must have
• This flyer must catch the eye of couples wanting to improve their relationship, and finances.
Nice to have
• Some space for us to plug in dates location and times. This flyer also has to have our funding statement at the bottom.

```html
<!DOCTYPE html>
<html lang="es">
<head>
<meta charset="utf-8">
<title>Talleres Para Parejas – Brightwell Bonds and Households Initiative</title>
<link href="https://fonts.googleapis.com/css2?family=Roboto+Condensed:ital,wght@0,400;1,700&family=Questrial&family=Cabin:wght@400;700&display=swap" rel="stylesheet">
<style>
  :root{
    --navy:#0f2f5c;
    --navy-deep:#14325e;
    --orange:#ee8a1c;
    --orange-band:#ea7d0d;
    --ink:#1c1c1c;
    --sky:#dce9f5;
    --page-bg:#e9ebee;
    --white:#ffffff;
  }
  *{box-sizing:border-box;margin:0;padding:0}
  html,body{width:1200px;height:1200px;overflow:hidden;background:var(--page-bg)}
  .flyer{
    position:absolute;left:176px;top:0;width:848px;height:1200px;overflow:hidden;
    background:linear-gradient(180deg,var(--white) 0px,var(--white) 120px,var(--sky) 330px,#eef4fa 520px,var(--white) 640px);
    font-family:"Cabin",sans-serif;color:var(--ink);
  }
  .brand{position:absolute;top:92px;left:0;width:100%;text-align:center}
  .brand-mark{display:block;margin:0 auto 8px;width:28px;height:28px;border-radius:50%;background:var(--orange)}
  .brand-name{font-family:"Cabin",sans-serif;font-weight:400;font-size:21px;color:var(--orange)}
  .brand-tagline{margin-top:6px;font-family:"Cabin",sans-serif;font-size:10.5px;letter-spacing:.4px;text-transform:uppercase;color:var(--navy);line-height:1.35}
  .title{position:absolute;top:176px;left:0;width:100%;text-align:center;
    font-family:"Roboto Condensed",sans-serif;font-style:italic;font-weight:700;font-size:82px;color:var(--navy);letter-spacing:-1px}
  .tagline{position:absolute;top:288px;left:0;width:100%;text-align:center;
    font-family:"Questrial",sans-serif;font-size:35px;line-height:44px;color:var(--orange)}
  .schedule{position:absolute;top:372px;left:0;width:100%;height:64px}
  .schedule .col{position:absolute;top:0}
  .schedule .date{right:443px;text-align:right}
  .schedule .time{left:443px;text-align:left}
  .schedule .divider{position:absolute;left:422px;top:4px;width:2px;height:56px;background:var(--ink)}
  .label{font-family:"Roboto Condensed",sans-serif;font-size:24px;color:var(--ink);line-height:30px}
  .value{font-family:"Cabin",sans-serif;font-weight:700;font-size:22px;color:var(--navy);line-height:30px}
  .location{position:absolute;top:454px;left:0;width:100%;text-align:center}
  .location .value{font-size:19.5px;line-height:25.5px}
  .note{position:absolute;top:572px;left:0;width:100%;text-align:center;font-family:"Questrial",sans-serif;font-size:26px;color:var(--ink)}
  .photo{position:absolute;left:382px;top:634px;width:466px;height:466px;
    background:radial-gradient(ellipse at 55% 45%,#f4efe9 0%,#e8d9c8 35%,#d9c1a3 55%,rgba(255,255,255,0) 72%)}
  .register{position:absolute;left:0;top:686px;width:557px;height:91px;background:var(--orange-band);color:var(--white);padding:10px 0 0 25px}
  .register h2{font-family:"Cabin",sans-serif;font-weight:700;font-size:18.5px;line-height:22px}
  .register p{font-size:15.5px;line-height:26px}
  .register .phone{display:flex;align-items:center;gap:5px;font-size:20px;line-height:22px}
  .topics{position:absolute;left:24px;top:790px;width:370px}
  .topics h3{font-family:"Cabin",sans-serif;font-weight:400;font-size:24px;color:var(--ink);margin-bottom:6px}
  .topics ul{list-style:none}
  .topics li{position:relative;padding-left:28px;font-size:15.5px;line-height:20.5px;margin-bottom:12px;color:var(--ink)}
  .topics li svg{position:absolute;left:0;top:3px}
  .funding{position:absolute;left:0;top:1100px;width:848px;height:100px;background:var(--navy-deep)}
  .funding p{position:absolute;left:27px;top:19px;width:510px;color:var(--white);font-size:11.4px;line-height:15.5px;text-align:justify}
  .partner{position:absolute;top:16px;height:60px;background:var(--white)}
  .partner-a{left:577px;width:118px}
  .partner-b{left:727px;width:101px}
</style>
</head>
<body>
<main class="flyer">
  <header class="brand">
    <span class="brand-mark"></span>
    <div class="brand-name">Brightwell Bonds and Households Initiative</div>
    <div class="brand-tagline">Fortalecimiento de relaciones | Capacitación financiera<br>y preparación laboral</div>
  </header>

  <h1 class="title">Talleres Para Parejas</h1>
  <p class="tagline">Porque una relación sana esta<br>“A Nuestro Alcance”</p>

  <section class="schedule">
    <div class="col date"><div class="label">Fecha de talleres</div><div class="value">Jueves Octubre 03, 12, 19, 26</div></div>
    <span class="divider"></span>
    <div class="col time"><div class="label">Horario:</div><div class="value">5:30pm –8:00pm</div></div>
  </section>

  <section class="location">
    <div class="label">Ubicación:</div>
    <div class="value">Rosewind Family Resource Center</div>
    <div class="value">2250 Alder Ave, Fairhaven CA 90000</div>
    <div class="value">(555) 214-3380</div>
  </section>

  <p class="note">*Cuidado de niños y cena será proporcionado</p>

  <div class="photo" role="img" aria-label="Foto de una pareja sonriente abrazándose, vestida de blanco"></div>

  <section class="register">
    <h2>Registración requerida Llámanos hoy!</h2>
    <p>Para más información llame a&nbsp; Rosewind Family Resource Center</p>
    <div class="phone">
      <svg width="17" height="17" viewBox="0 0 20 20" aria-hidden="true"><circle cx="10" cy="10" r="9" fill="none" stroke="#1c1c1c" stroke-width="1.6"/><path d="M7 5.5l1.6 2.4-1 1c.6 1.3 1.5 2.2 2.6 2.8l1-1 2.3 1.6-.9 1.7c-3.2-.4-6-3.3-6.3-6.6z" fill="#1c1c1c"/></svg>
      <span>(555) 214-3391</span>
    </div>
  </section>

  <section class="topics">
    <h3>Temas incluyen:</h3>
    <ul>
      <li><svg width="20" height="14" viewBox="0 0 20 14" aria-hidden="true"><circle cx="7" cy="8" r="5" fill="none" stroke="#0f2f5c" stroke-width="1.6"/><circle cx="13" cy="8" r="5" fill="none" stroke="#0f2f5c" stroke-width="1.6"/></svg>Llaves para la buena&nbsp; communicación</li>
      <li><svg width="20" height="14" viewBox="0 0 20 14" aria-hidden="true"><circle cx="7" cy="8" r="5" fill="none" stroke="#0f2f5c" stroke-width="1.6"/><circle cx="13" cy="8" r="5" fill="none" stroke="#0f2f5c" stroke-width="1.6"/></svg>Tipos de personalidad y expectativas</li>
      <li><svg width="20" height="14" viewBox="0 0 20 14" aria-hidden="true"><circle cx="7" cy="8" r="5" fill="none" stroke="#0f2f5c" stroke-width="1.6"/><circle cx="13" cy="8" r="5" fill="none" stroke="#0f2f5c" stroke-width="1.6"/></svg>Señales de peligro en una relación</li>
      <li><svg width="20" height="14" viewBox="0 0 20 14" aria-hidden="true"><circle cx="7" cy="8" r="5" fill="none" stroke="#0f2f5c" stroke-width="1.6"/><circle cx="13" cy="8" r="5" fill="none" stroke="#0f2f5c" stroke-width="1.6"/></svg>Técnicas para formar y&nbsp; sostener una<br>relación sana</li>
      <li><svg width="20" height="14" viewBox="0 0 20 14" aria-hidden="true"><circle cx="7" cy="8" r="5" fill="none" stroke="#0f2f5c" stroke-width="1.6"/><circle cx="13" cy="8" r="5" fill="none" stroke="#0f2f5c" stroke-width="1.6"/></svg>Resolucion de problemas</li>
      <li><svg width="20" height="14" viewBox="0 0 20 14" aria-hidden="true"><circle cx="7" cy="8" r="5" fill="none" stroke="#0f2f5c" stroke-width="1.6"/><circle cx="13" cy="8" r="5" fill="none" stroke="#0f2f5c" stroke-width="1.6"/></svg>Como mantener la diversion</li>
      <li><svg width="20" height="14" viewBox="0 0 20 14" aria-hidden="true"><circle cx="7" cy="8" r="5" fill="none" stroke="#0f2f5c" stroke-width="1.6"/><circle cx="13" cy="8" r="5" fill="none" stroke="#0f2f5c" stroke-width="1.6"/></svg>Como adminstrar el dinero entre pareja Y<br>muchos mas</li>
    </ul>
  </section>

  <footer class="funding">
    <p>“Funding for this project was provided by the Federal Office of Family Services, Division for Children and Households, Grant: #00FS0000.These services are avaiable to all eligible persons, regardless of race, gender, age, disability, or religion.”</p>
    <div class="partner partner-a" role="img" aria-label="Insignia de organización asociada"></div>
    <div class="partner partner-b" role="img" aria-label="Insignia de organización asociada"></div>
  </footer>
</main>
</body>
</html>
```